Orbit 528 - Pagevo Book Cover

I am looking for a Pagevo book cover for my book about "Orbit 528".
The Book is Titled:
Orbit 528 Advanced
Shaping Tomorrow: Paths Toward Unlocking Hidden Cosmic Laws
Author is Dorian Welby
Here is a book description that may help you understand more about it:
Inspired by the genius of Anton Brevik, this comprehensive guide delves into the ancient wisdom and cutting-edge science behind the 369 method, a powerful tool for manifesting your desires. Whether you're seeking personal growth, financial success, or spiritual enlightenment, this book provides advanced techniques and methods to transform your dreams into reality.
Any questions please ask.
Thanks
Colin

```html
<!DOCTYPE html>
<html lang="en">
<head>
<meta charset="utf-8">
<title>Orbit 528 – Book Cover</title>
<link rel="stylesheet" href="https://fonts.googleapis.com/css2?family=Marcellus&family=Cormorant+SC:wght@500&display=swap">
<style>
  :root {
    --page-bg: #d7d7d7;
    --cover-deep: #2a1740;
    --cover-violet: #5b2a73;
    --cover-magenta: #a3407a;
    --cover-glow: #e49a5c;
    --cover-teal: #2f6f8e;
    --cover-night: #1e1233;
    --type-peach: #f7ddd0;
  }
  * { margin: 0; padding: 0; box-sizing: border-box; }
  html, body {
    width: 1200px; height: 1200px; overflow: hidden;
    background: var(--page-bg);
  }
  .canvas { position: relative; width: 1200px; height: 1200px; }
  .book-cover {
    position: absolute; left: 258px; top: 54px;
    width: 684px; height: 1092px; overflow: hidden;
    color: var(--type-peach);
    text-align: center;
  }
  .cover-art {
    position: absolute; inset: 0;
    background:
      radial-gradient(circle at 50% 45%, var(--cover-glow) 0%, #c8636a 14%, var(--cover-magenta) 26%, var(--cover-violet) 42%, transparent 62%),
      radial-gradient(ellipse at 70% 12%, var(--cover-teal) 0%, transparent 45%),
      radial-gradient(ellipse at 15% 60%, #2c4f86 0%, transparent 40%),
      linear-gradient(180deg, var(--cover-deep) 0%, var(--cover-violet) 40%, var(--cover-deep) 80%, var(--cover-night) 100%);
  }
  .subtitle {
    position: absolute; left: 0; right: 0; top: 262px;
    font-family: "Cormorant SC", serif; font-weight: 500;
    font-size: 13px; line-height: 22px; letter-spacing: 0.04em;
  }
  .title {
    position: absolute; left: 0; right: 0; top: 300px;
    font-family: "Marcellus", serif; font-weight: 400;
  }
  .title-word {
    display: block; font-size: 76px; line-height: 88px;
    letter-spacing: 0.12em; padding-left: 0.12em;
  }
  .title-number {
    display: block; font-size: 128px; line-height: 124px;
    letter-spacing: 0.01em;
  }
  .author {
    position: absolute; left: 0; right: 0; top: 940px;
    font-family: "Marcellus", serif; font-size: 42px;
    letter-spacing: 0.1em; padding-left: 0.1em;
  }
</style>
</head>
<body>
  <main class="canvas">
    <section class="book-cover">
      <div class="cover-art" role="img" aria-label="Cosmic illustration: swirling purple, blue and orange galaxy with planets, and a silhouetted figure meditating at the bottom"></div>
      <p class="subtitle">SHAPING TOMORROW<br>PATHS TOWARD UNLOCKING HIDDEN COSMIC LAWS</p>
      <h1 class="title">
        <span class="title-word">ORBIT</span>
        <span class="title-number">528</span>
      </h1>
      <p class="author">DORIAN WELBY</p>
    </section>
  </main>
</body>
</html>
```